American cannabis tech company business card design

Thrum.com is seeking a modern, professional, and brand-aligned business card that represents our company and its core values: Mission, Story, Values, and Impact. As an innovative cannabis company, we want a business card that is not only visually appealing but also serves as a representation of who we are and what we stand for.

Project Scope: Design a double-sided business card that integrates our brand identity and core values. Incorporate our key brand elements, ensuring a sleek and contemporary aesthetic. Visually reflect our core values (Mission, Story, Values, Impact) in a way that is engaging yet professional.

Target Market(s)

Vendors, third parties,

Contact Information for Business Card

Contact details (name, title, email, phone, website, etc.)

Font styles to use
Other font styles liked:
• Caslon, Centra

Colors

Designer to choose colors to be used in the design.

Requirements
Must have
• Thrum.com logo and branding A creative yet clean way to integrate our core values (Mission, Story, Values, Impact) Modern typography and a well-structured layout
Nice to have
• forest green, grey, white, black
Should not have
• references to marijuana, leafs, plants, or related product

```html
<!DOCTYPE html>
<html lang="en">
<head>
<meta charset="utf-8">
<title>Thrum.com Business Card</title>
<link rel="stylesheet" href="https://fonts.googleapis.com/css2?family=Arimo:wght@400;700&display=swap">
<style>
  :root {
    --page-bg: #e6e7e5;
    --card-bg: #ffffff;
    --brand-dark: #14301a;
    --brand-band: #3f6140;
    --text-grey: #555a56;
    --shadow: rgba(0, 0, 0, 0.18);
  }
  * { margin: 0; padding: 0; box-sizing: border-box; }
  html, body {
    width: 1200px;
    height: 900px;
    overflow: hidden;
    background: var(--page-bg);
    font-family: "Arimo", Arial, sans-serif;
  }
  .canvas {
    width: 1200px;
    height: 900px;
    display: flex;
    flex-direction: column;
    align-items: center;
    justify-content: center;
    gap: 40px;
  }
  .card {
    position: relative;
    width: 665px;
    height: 380px;
    background: var(--card-bg);
    box-shadow: 0 10px 28px var(--shadow);
    overflow: hidden;
  }
  .card__band {
    position: absolute;
    left: 0;
    right: 0;
    bottom: 0;
    height: 28px;
    background: var(--brand-band);
  }
  .wordmark {
    position: absolute;
    bottom: 26px;
    font-weight: 700;
    color: var(--brand-dark);
    letter-spacing: -2px;
    line-height: 1;
  }
  .card--front .wordmark {
    right: 40px;
    font-size: 118px;
  }
  .card--back .wordmark {
    left: 36px;
    font-size: 104px;
  }
  .contact {
    position: absolute;
    top: 40px;
    right: 38px;
    text-align: right;
    color: var(--text-grey);
  }
  .contact__name {
    font-weight: 700;
    font-size: 21px;
    color: var(--brand-dark);
    letter-spacing: 0.3px;
  }
  .contact__title {
    font-size: 17px;
    margin-top: 2px;
  }
  .contact__list {
    list-style: none;
    margin-top: 22px;
    font-size: 17px;
  }
  .contact__item {
    display: flex;
    justify-content: flex-end;
    align-items: center;
    gap: 8px;
    margin-bottom: 8px;
  }
  .contact__icon {
    width: 18px;
    height: 18px;
    flex: none;
  }
</style>
</head>
<body>
<main class="canvas">
  <section class="card card--front" aria-label="Business card front">
    <div class="wordmark">THRUM</div>
    <div class="card__band"></div>
  </section>

  <section class="card card--back" aria-label="Business card back">
    <div class="contact">
      <p class="contact__name">OWEN HARTLEY</p>
      <p class="contact__title">Co-founder &amp; CEO</p>
      <ul class="contact__list">
        <li class="contact__item">
          <span>000-000-0000</span>
          <svg class="contact__icon" viewBox="0 0 24 24" aria-hidden="true">
            <path fill="#14301a" d="M6.6 10.8a15 15 0 0 0 6.6 6.6l2.2-2.2a1 1 0 0 1 1-.25 11.4 11.4 0 0 0 3.6.57 1 1 0 0 1 1 1V20a1 1 0 0 1-1 1A17 17 0 0 1 3 4a1 1 0 0 1 1-1h3.5a1 1 0 0 1 1 1c0 1.25.2 2.45.57 3.6a1 1 0 0 1-.25 1z"/>
          </svg>
        </li>
        <li class="contact__item">
          <span>owen@thrum.com</span>
          <svg class="contact__icon" viewBox="0 0 24 24" aria-hidden="true">
            <rect x="2" y="5" width="20" height="14" fill="#14301a"/>
            <path d="M2.5 5.5 12 13l9.5-7.5" fill="none" stroke="#ffffff" stroke-width="1.5"/>
          </svg>
        </li>
        <li class="contact__item">
          <span>www.thrum.com</span>
          <svg class="contact__icon" viewBox="0 0 24 24" aria-hidden="true">
            <circle cx="12" cy="12" r="10" fill="#3f6140"/>
            <g fill="none" stroke="#ffffff" stroke-width="1.2">
              <ellipse cx="12" cy="12" rx="4" ry="10"/>
              <path d="M2 12h20M4 7h16M4 17h16M12 2v20"/>
            </g>
          </svg>
        </li>
      </ul>
    </div>
    <div class="wordmark">THRUM</div>
    <div class="card__band"></div>
  </section>
</main>
</body>
</html>
```